Creat new BusinessCard for Brightfold Consulting!

Hello Creativ Designer. I need a new Businesscard for our brand new Company "Brightfold Training". We do Consulting for a better Life & Work Situation. to create Fulfillment, Sense, Motivation and healthy Work Places in Company's. So we try to create a better World and help the employee to like what they do!
So we would like to have 2 Sites on the card. On the Back we want to put this words: "The true purpose of work, is to lift each other" (it can be vertical oder horizontal). In the front there is the Logo (Black or White) and Adress+ and Slogan.

Slogan on the front: -Shape your Work & Life into a brighter place-

Name: Lukas Verhoff
Titel: Founder - Visionary - Trainer
Adress: Based in Switzerland

Tel: +41 (0) 71 583 42 17
Email: hello@brightfold-training.ch
Homepage: www.brightfold-training.ch

Thanks for your inspired Ideas and your help to make the world to a better place! IT has to be ready to print and normal Size.

Target Market(s)

insurance, Bank, Telecom, industry, IT, Medical

Contact Information for Business Card

Breite: 85 mm x Höhe: 55 mm

Colors

Designer to choose colors to be used in the design.

Requirements
Nice to have
• Thanks for your Ideas so far!
• Maybe you can try/play with the colors: Purple Code #652C8F and Grey #979797 from the Zelvor Logo purple and grey (but only a soft combination, not to much)

```html
<!DOCTYPE html>
<html lang="en">
<head>
<meta charset="utf-8">
<title>Brightfold Training – Business Card</title>
<link href="https://fonts.googleapis.com/css2?family=Montserrat:wght@600&family=Roboto:ital,wght@0,400;0,700;1,400&family=Roboto+Condensed:wght@700&display=swap" rel="stylesheet">
<style>
  :root {
    --bg: #e8e5e1;
    --card-black: #030303;
    --card-white: #ffffff;
    --circle-tint: #f1f1f1;
    --ring-grey: #7a7a7a;
    --mark-faint: #1a1a1a;
    --text-light: #ffffff;
    --text-dark: #111111;
  }
  html, body {
    margin: 0;
    padding: 0;
    width: 1200px;
    height: 960px;
    overflow: hidden;
    background: var(--bg);
  }
  .canvas {
    position: relative;
    width: 1200px;
    height: 960px;
  }
  .card {
    position: absolute;
    width: 600px;
    height: 342px;
    border-radius: 18px;
    overflow: hidden;
    background: var(--card-black);
    box-shadow: 0 3px 8px rgba(0,0,0,0.25);
  }
  .card--front { left: 314px; top: 113px; }
  .card--back  { left: 312px; top: 472px; }
  .card__art {
    position: absolute;
    inset: 0;
  }
  .holder {
    position: absolute;
    left: 27px;
    top: 68px;
    color: var(--text-light);
    font-family: "Roboto", sans-serif;
  }
  .holder__name {
    margin: 0;
    font-size: 20px;
    font-weight: 700;
    line-height: 1.1;
  }
  .holder__title {
    margin: 3px 0 0;
    font-size: 14px;
    font-weight: 400;
  }
  .slogan {
    position: absolute;
    left: 26px;
    top: 169px;
    margin: 0;
    color: var(--text-light);
    font-family: "Roboto", sans-serif;
    font-style: italic;
    font-size: 14px;
    line-height: 19px;
  }
  .contact {
    position: absolute;
    left: 28px;
    top: 216px;
    margin: 0;
    padding: 0;
    list-style: none;
    color: var(--text-light);
    font-family: "Roboto", sans-serif;
    font-size: 14.5px;
    line-height: 19px;
  }
  .contact__item {
    display: flex;
    align-items: center;
    gap: 8px;
  }
  .contact__icon {
    width: 13px;
    height: 13px;
    fill: var(--text-light);
  }
  .brand {
    position: absolute;
    font-family: "Montserrat", sans-serif;
    font-weight: 600;
    text-align: center;
    line-height: 1;
  }
  .brand--front {
    left: 346px;
    top: 203px;
    width: 210px;
    color: var(--text-dark);
  }
  .brand__name { display: block; font-size: 27px; letter-spacing: 0.5px; }
  .brand__sub  { display: block; margin-top: 7px; font-size: 13px; letter-spacing: 3px; }
  .brand--back {
    right: 22px;
    top: 245px;
    color: var(--text-light);
    text-align: right;
  }
  .brand--back .brand__name { font-size: 36px; }
  .brand--back .brand__sub  { font-size: 16px; letter-spacing: 4.5px; text-align: center; margin-top: 7px; }
  .motto {
    position: absolute;
    right: 20px;
    top: 306px;
    margin: 0;
    color: var(--text-light);
    font-family: "Roboto Condensed", sans-serif;
    font-weight: 700;
    font-size: 13.5px;
  }
</style>
</head>
<body>
<main class="canvas">

  <section class="card card--front" aria-label="Card front">
    <svg class="card__art" width="600" height="342" viewBox="0 0 600 342" aria-hidden="true">
      <circle cx="456" cy="172" r="188" fill="var(--ring-grey)"/>
      <circle cx="463" cy="172" r="183" fill="var(--card-white)"/>
      <circle cx="470" cy="172" r="160" fill="var(--circle-tint)"/>
      <circle cx="451" cy="142" r="51" fill="var(--card-black)"/>
    </svg>

    <div class="holder">
      <h1 class="holder__name">LUKAS VERHOFF</h1>
      <p class="holder__title">FOUNDER - VISIONARY - TRAINER</p>
    </div>

    <p class="slogan">Shape your Work<br>&amp; Life into a brighter place</p>

    <ul class="contact">
      <li class="contact__item">
        <svg class="contact__icon" viewBox="0 0 24 24"><path d="M6.6 10.8a15.1 15.1 0 0 0 6.6 6.6l2.2-2.2a1 1 0 0 1 1-.25 11.4 11.4 0 0 0 3.6.57 1 1 0 0 1 1 1V20a1 1 0 0 1-1 1A17 17 0 0 1 3 4a1 1 0 0 1 1-1h3.5a1 1 0 0 1 1 1c0 1.25.2 2.45.57 3.57a1 1 0 0 1-.25 1z"/></svg>
        <span>+41 (0) 71 583 42 17</span>
      </li>
      <li class="contact__item">
        <svg class="contact__icon" viewBox="0 0 24 24"><path d="M2 5h20v14H2z"/><path d="M3 6l9 7 9-7" stroke="var(--card-black)" stroke-width="2" fill="none"/></svg>
        <span>hello@brightfold-training.ch</span>
      </li>
      <li class="contact__item">
        <svg class="contact__icon" viewBox="0 0 24 24"><circle cx="12" cy="12" r="10"/><path d="M2 12h20M12 2c3 3 3 17 0 20M12 2c-3 3-3 17 0 20" stroke="var(--card-black)" stroke-width="1.6" fill="none"/></svg>
        <span>www.brightfold-training.ch</span>
      </li>
    </ul>

    <div class="brand brand--front">
      <span class="brand__name">BRIGHTFOLD</span>
      <span class="brand__sub">TRAINING</span>
    </div>
  </section>

  <section class="card card--back" aria-label="Card back">
    <svg class="card__art" width="600" height="342" viewBox="0 0 600 342" aria-hidden="true">
      <circle cx="166" cy="171" r="160" fill="var(--mark-faint)"/>
    </svg>

    <div class="brand brand--back">
      <span class="brand__name">BRIGHTFOLD</span>
      <span class="brand__sub">TRAINING</span>
    </div>

    <p class="motto">The true purpose of work, is to lift each other</p>
  </section>

</main>
</body>
</html>
```